Granite Ridge Response Business Card

Side 1: Granite Ridge Response Logo (logo without Maltese cross) with industrial rope rescue related theme. Our company services - TRAINING - Fire Training, Confined Space Rescue Training, Rope Rescue training, Hazmat Training, Incident Command, EMS, Pump Operations Training. Website - graniteridgeresponse.example.
Side 2: Granite Ridge Response Fire Department Logo (logo with Maltese cross) with Firefighter related theme. Company (division) services - FIELD SERVICES - Fire Department, Stand-by Rescue, Safety, EMS, Planning. "Supporting the Emergency Response Community Since 1967"

Add contact information wherever it makes since (Name, Email, Phone).
I would like it to represent the Granite Ridge Response Fire Department Logo as a division not as a separate entity without saying it, possibly by depicting it in the background of Side 2 instead of being a standalone picture like the logo on Side 1.

```html
<!DOCTYPE html>
<html lang="en">
<head>
<meta charset="utf-8">
<title>Granite Ridge Response Business Cards</title>
<link href="https://fonts.googleapis.com/css2?family=Montserrat:wght@500;600;800&family=Oswald:wght@500;600&display=swap" rel="stylesheet">
<style>
  :root {
    --red: #ee1c24;
    --ink: #1e1e1e;
    --band: #1b1b1b;
    --white: #ffffff;
    --stage: #3b3b3d;
    --muted: #2c2c2c;
  }
  * { box-sizing: border-box; margin: 0; padding: 0; }
  html, body { width: 1200px; height: 1200px; overflow: hidden; }
  body {
    background: var(--stage);
    display: flex;
    flex-direction: column;
    align-items: center;
    justify-content: center;
    gap: 44px;
    font-family: "Montserrat", sans-serif;
  }
  .card {
    position: relative;
    width: 900px;
    height: 514px;
    border-radius: 26px;
    overflow: hidden;
    background: var(--white);
    box-shadow: 0 10px 30px rgba(0,0,0,.35);
  }
  .card__photo { position: absolute; inset: 0 0 182px 0; }
  .card--field .card__photo {
    background: linear-gradient(90deg, #d9c48a 0%, #e6cf8f 22%, #efe2bd 40%, rgba(255,255,255,0) 62%);
  }
  .card--training .card__photo {
    background: linear-gradient(100deg, #e4e8f0 0%, #f5f7fa 40%, #e2e4e8 70%, #c9ccd2 100%);
  }
  .brand {
    position: absolute;
    right: 56px;
    top: 86px;
    text-align: right;
    font-family: "Montserrat", sans-serif;
    font-weight: 800;
    font-size: 36px;
    line-height: 1.1;
    letter-spacing: 2px;
    text-transform: uppercase;
  }
  .card--field .brand { color: var(--ink); }
  .card--training .brand { color: var(--red); }
  .contact { position: absolute; left: 62px; top: 120px; }
  .contact__name {
    color: var(--red);
    font-weight: 800;
    font-size: 46px;
    line-height: 1;
    letter-spacing: -0.5px;
  }
  .contact__role {
    color: var(--ink);
    font-weight: 500;
    font-size: 22px;
    letter-spacing: 1px;
    margin: 4px 0 12px 6px;
  }
  .contact__list { list-style: none; }
  .contact__item {
    display: flex;
    align-items: center;
    gap: 12px;
    color: var(--ink);
    font-weight: 600;
    font-size: 19px;
    line-height: 32px;
  }
  .contact__item svg { width: 22px; height: 22px; flex: none; }
  .services-label {
    position: absolute;
    left: 440px;
    top: 270px;
    font-family: "Oswald", sans-serif;
    font-weight: 600;
    font-size: 26px;
    color: var(--muted);
    letter-spacing: .5px;
  }
  .rule {
    position: absolute;
    left: 0; right: 0;
    top: 316px;
    height: 4px;
    background: var(--red);
  }
  .band {
    position: absolute;
    left: 0; right: 0; bottom: 0;
    height: 182px;
    background: var(--band);
    padding: 28px 30px 0 180px;
    font-family: "Oswald", sans-serif;
    text-transform: uppercase;
  }
  .band__title {
    color: var(--red);
    font-weight: 600;
    font-size: 28px;
    line-height: 1.15;
  }
  .band__line {
    color: var(--white);
    font-weight: 500;
    font-size: 21px;
    line-height: 1.45;
    white-space: nowrap;
  }
  .dot { color: var(--red); padding: 0 4px; }
</style>
</head>
<body>

<section class="card card--field">
  <div class="card__photo" role="img" aria-label="Photo of two firefighters in helmets and turnout gear handling a hose, fading to white"></div>
  <div class="brand">Granite Ridge<br>Response</div>
  <div class="contact">
    <div class="contact__name">FULL NAME</div>
    <div class="contact__role">POSITION</div>
    <ul class="contact__list">
      <li class="contact__item">
        <svg viewBox="0 0 24 24" aria-hidden="true"><path fill="#ee1c24" d="M6.6 10.8a15 15 0 0 0 6.6 6.6l2.2-2.2c.3-.3.7-.4 1-.2 1.1.4 2.3.6 3.6.6.6 0 1 .4 1 1V20c0 .6-.4 1-1 1A17 17 0 0 1 3 4c0-.6.4-1 1-1h3.5c.6 0 1 .4 1 1 0 1.3.2 2.5.6 3.6.1.3 0 .7-.2 1z"/></svg>
        000 000 0000
      </li>
      <li class="contact__item">
        <svg viewBox="0 0 24 24" aria-hidden="true"><rect x="2" y="5" width="20" height="14" fill="#ee1c24"/><path d="M2 5l10 8 10-8" fill="none" stroke="#fff" stroke-width="2"/></svg>
        info@graniteridgeresponse.example
      </li>
      <li class="contact__item">
        <svg viewBox="0 0 24 24" aria-hidden="true"><g fill="none" stroke="#ee1c24" stroke-width="2"><circle cx="12" cy="12" r="9"/><ellipse cx="12" cy="12" rx="4" ry="9"/><path d="M3 12h18M5 7h14M5 17h14"/></g></svg>
        graniteridgeresponse.example
      </li>
    </ul>
  </div>
  <div class="services-label">SERVICES</div>
  <div class="rule"></div>
  <div class="band">
    <div class="band__title">Field Services</div>
    <div class="band__line">Fire Department<span class="dot">•</span>Stand-by Rescue<span class="dot">•</span>Safety<span class="dot">•</span>EMS<span class="dot">•</span>Planning</div>
    <div class="band__line">"Supporting the Emergency Response Community Since 1967"</div>
  </div>
</section>

<section class="card card--training">
  <div class="card__photo" role="img" aria-label="Photo of a rescuer descending on ropes beside an industrial tower, pale grey tones"></div>
  <div class="brand">Granite Ridge<br>Response</div>
  <div class="contact">
    <div class="contact__name">FULL NAME</div>
    <div class="contact__role">POSITION</div>
    <ul class="contact__list">
      <li class="contact__item">
        <svg viewBox="0 0 24 24" aria-hidden="true"><path fill="#ee1c24" d="M6.6 10.8a15 15 0 0 0 6.6 6.6l2.2-2.2c.3-.3.7-.4 1-.2 1.1.4 2.3.6 3.6.6.6 0 1 .4 1 1V20c0 .6-.4 1-1 1A17 17 0 0 1 3 4c0-.6.4-1 1-1h3.5c.6 0 1 .4 1 1 0 1.3.2 2.5.6 3.6.1.3 0 .7-.2 1z"/></svg>
        000 000 0000
      </li>
      <li class="contact__item">
        <svg viewBox="0 0 24 24" aria-hidden="true"><rect x="2" y="5" width="20" height="14" fill="#ee1c24"/><path d="M2 5l10 8 10-8" fill="none" stroke="#fff" stroke-width="2"/></svg>
        info@graniteridgeresponse.example
      </li>
      <li class="contact__item">
        <svg viewBox="0 0 24 24" aria-hidden="true"><g fill="none" stroke="#ee1c24" stroke-width="2"><circle cx="12" cy="12" r="9"/><ellipse cx="12" cy="12" rx="4" ry="9"/><path d="M3 12h18M5 7h14M5 17h14"/></g></svg>
        graniteridgeresponse.example
      </li>
    </ul>
  </div>
  <div class="services-label">SERVICES</div>
  <div class="rule"></div>
  <div class="band">
    <div class="band__title">Training</div>
    <div class="band__line">Fire Training<span class="dot">•</span>Confined Space Rescue Training<span class="dot">•</span>Rope Rescue Training</div>
    <div class="band__line">Hazmat Training<span class="dot">•</span>Incident Command<span class="dot">•</span>EMS<span class="dot">•</span>Pump Operations Training</div>
  </div>
</section>

</body>
</html>
```